Covid19 Poster for workplaces

Create a poster on how to protect yourself from Corona virus at work.
We are a Kindred Works company. We have just re-branded so we need to fit in with our brand. We like clean and fresh, slightly amusing is ok if it will draw attention but it's an important topic. A4 and A3 please.

Content:

Headline: Lower the risk of COVID 19 in the workplace.

BE WELL

Bring your own cup - don’t share cups and food.
Elbow tap instead of handshakes and kisses
Wash your hands often - with soap.
Elbow or tissues when you cough or sneeze then straight in the bin
Leave your face alone after touching shared surfaces
Leave your bugs at home if you’re feeling unwell.

Call health line if you have a cough, a high temperature and shortness of breath. 0800 472 9160

Based on recommendations from ZPK and QLN

Target Market(s)

Employees - so anyone

Other font styles liked:
• Use the closest font to the brand documents

Requirements
Should not have
• Clip art

```html
<!DOCTYPE html>
<html lang="en">
<head>
<meta charset="utf-8">
<title>Lower the risk of COVID-19 in the workplace</title>
<link href="https://fonts.googleapis.com/css2?family=Poppins:wght@400;600;700;800&display=swap" rel="stylesheet">
<style>
  :root{
    --teal:#43e3b4;
    --ink:#1b1b1b;
    --pink:#f0476a;
    --white:#ffffff;
    --stage:#474747;
    --rule:#2a2a2a;
  }
  *{box-sizing:border-box;margin:0;padding:0}
  html,body{width:1200px;height:1084px;overflow:hidden}
  body{background:var(--stage);font-family:'Poppins',sans-serif;position:relative}
  .poster{position:absolute;left:231px;top:20px;width:738px;height:1044px;background:var(--white);overflow:hidden}
  .header{position:absolute;left:0;top:0;width:738px;height:247px;background:var(--teal)}
  .header-title{position:absolute;left:65px;top:40px;color:var(--white);font-weight:800;font-size:47px;line-height:44px;letter-spacing:-0.5px}
  .header-url{position:absolute;left:69px;top:202px;color:var(--white);font-weight:600;font-size:13.5px}
  .team-photo{position:absolute;left:341px;top:31px;width:361px;height:195px;border-radius:90px;
    background:linear-gradient(120deg,#3b3f3c 0%,#6b5a4a 30%,#2e5bb8 50%,#d9a63a 62%,#2d2f31 100%)}
  .headline{position:absolute;left:65px;top:284px;font-weight:700;font-size:40px;line-height:50px;letter-spacing:-0.5px}
  .headline .accent{color:var(--teal)}
  .headline .dark{color:var(--ink)}
  .tips{position:absolute;left:65px;top:418px;width:412px;list-style:none}
  .tip{position:relative;height:65.4px;border-bottom:1px solid var(--rule)}
  .tip:last-child{border-bottom:none}
  .tip-icon{position:absolute;left:0;top:6px;width:50px;height:50px}
  .tip-title{position:absolute;left:81px;top:6px;color:var(--teal);font-weight:700;font-size:22px;line-height:26px;white-space:nowrap}
  .tip-note{position:absolute;left:81px;top:36px;color:var(--ink);font-size:11px;white-space:nowrap}
  .call-shape{position:absolute;left:0;top:0}
  .phone{position:absolute;left:72px;top:896px;color:var(--white);font-weight:700;font-size:39px;letter-spacing:1px}
  .call-text{position:absolute;left:72px;top:945px;color:var(--ink);font-weight:700;font-size:16.5px;line-height:19px}
  .partners{position:absolute;left:72px;top:991px;display:flex;gap:14px;color:var(--white);font-weight:600;font-size:10px}
  .partners span{display:flex;align-items:center;gap:4px}
  .partners i{display:inline-block;width:13px;height:13px;border-radius:50%;background:rgba(255,255,255,.85)}
  .source{position:absolute;left:72px;top:1017px;color:var(--white);font-size:9px}
  .brand{position:absolute;left:531px;top:972px;display:flex;align-items:center;gap:9px}
  .brand-dot{width:40px;height:40px;border-radius:50%;background:var(--teal)}
  .brand-name{color:var(--ink);font-weight:700;font-size:20px;line-height:19px}
</style>
</head>
<body>
<main class="poster">
  <header class="header">
    <h1 class="header-title">Wellbeing<br>matters at<br>work</h1>
    <p class="header-url">www.kindredworks.co.nz</p>
    <div class="team-photo" role="img" aria-label="Photo of smiling colleagues working together at their desks"></div>
  </header>

  <h2 class="headline"><span class="accent">Lower the risk of COVID-19</span><br><span class="dark">in the workplace</span></h2>

  <ul class="tips">
    <li class="tip">
      <svg class="tip-icon" viewBox="0 0 50 50" role="img" aria-label="Shared cup and cutlery icon, crossed out">
        <circle cx="30" cy="20" r="15" fill="#43e3b4"/>
        <path d="M4 34 L18 48 M18 34 L4 48" stroke="#f0476a" stroke-width="5" stroke-linecap="round"/>
      </svg>
      <div class="tip-title">NO SHARING</div>
      <div class="tip-note">bring your own cup - don’t share cups and food</div>
    </li>
    <li class="tip">
      <svg class="tip-icon" viewBox="0 0 50 50" role="img" aria-label="Handshake icon, crossed out">
        <circle cx="30" cy="20" r="15" fill="#43e3b4"/>
        <path d="M4 34 L18 48 M18 34 L4 48" stroke="#f0476a" stroke-width="5" stroke-linecap="round"/>
      </svg>
      <div class="tip-title">ELBOW TAP</div>
      <div class="tip-note">instead of handshakes</div>
    </li>
    <li class="tip">
      <svg class="tip-icon" viewBox="0 0 50 50" role="img" aria-label="Hand washing icon, ticked">
        <circle cx="30" cy="20" r="15" fill="#43e3b4"/>
        <path d="M4 44 L10 49 L24 34" fill="none" stroke="#f0476a" stroke-width="5" stroke-linecap="round" stroke-linejoin="round"/>
      </svg>
      <div class="tip-title">WASH YOUR HANDS OFTEN</div>
      <div class="tip-note">with soap for 20 seconds</div>
    </li>
    <li class="tip">
      <svg class="tip-icon" viewBox="0 0 50 50" role="img" aria-label="Sneezing icon, crossed out">
        <circle cx="30" cy="20" r="15" fill="#43e3b4"/>
        <path d="M4 34 L18 48 M18 34 L4 48" stroke="#f0476a" stroke-width="5" stroke-linecap="round"/>
      </svg>
      <div class="tip-title">USE YOUR ELBOW OR TISSUES</div>
      <div class="tip-note">when you cough or sneeze and put tissues in the bin immediately</div>
    </li>
    <li class="tip">
      <svg class="tip-icon" viewBox="0 0 50 50" role="img" aria-label="Touching face icon, crossed out">
        <circle cx="30" cy="20" r="15" fill="#43e3b4"/>
        <path d="M4 34 L18 48 M18 34 L4 48" stroke="#f0476a" stroke-width="5" stroke-linecap="round"/>
      </svg>
      <div class="tip-title">LEAVE YOUR FACE ALONE</div>
      <div class="tip-note">after touching shared spaces</div>
    </li>
    <li class="tip">
      <svg class="tip-icon" viewBox="0 0 50 50" role="img" aria-label="House icon, ticked">
        <path d="M24 4 L44 22 L38 22 L38 42 L12 42 L12 22 L4 22 Z" fill="#43e3b4"/>
        <path d="M4 44 L10 49 L24 34" fill="none" stroke="#f0476a" stroke-width="5" stroke-linecap="round" stroke-linejoin="round"/>
      </svg>
      <div class="tip-title">STAY AT HOME</div>
      <div class="tip-note">if you’re feeling unwell</div>
    </li>
  </ul>

  <svg class="call-shape" width="738" height="1044" viewBox="0 0 738 1044" aria-hidden="true">
    <path d="M0 904 C90 860 190 839 275 839 C400 839 500 890 496 956 C494 990 485 1020 472 1044 L0 1044 Z" fill="#43e3b4"/>
  </svg>
  <div class="phone">0800 472 9160</div>
  <p class="call-text">Call Careline if you have a cough, a high<br>temperature and shortness of breath.</p>
  <div class="partners"><span><i></i>ZPK</span><span><i></i>QLN</span></div>
  <p class="source">Based on recommendations from ZPK and QLN</p>

  <div class="brand">
    <div class="brand-dot"></div>
    <div class="brand-name">Kindred<br>Works</div>
  </div>
</main>
</body>
</html>
```